Awesome photographers card for an awesome new business

Double sided business card Black background and silver logo in middle on one side. Details on otherside. please keep it simple

Photographer

Gavin Tolley
0482615073
GavinTolleyPhotography82@lumenpost.com
www.GavinTolleyPhotography.com.au
Instagram _Gavin_tolley

Requirements
Must have
• My logo in Silver
• please use instagram logo instead of "Instagram"

```html
<!DOCTYPE html>
<html lang="en">
<head>
<meta charset="utf-8">
<title>Gavin Tolley Photography – Business Card</title>
<link rel="stylesheet" href="https://fonts.googleapis.com/css2?family=Questrial&display=swap">
<style>
  :root {
    --canvas: #ffffff;
    --card: #000000;
    --silver: #c9c9c9;
    --text: #ffffff;
  }
  * { margin: 0; padding: 0; box-sizing: border-box; }
  html, body {
    width: 1200px;
    height: 1000px;
    overflow: hidden;
    background: var(--canvas);
  }
  .sheet {
    position: relative;
    width: 1200px;
    height: 1000px;
    display: flex;
    justify-content: center;
    align-items: center;
    gap: 6px;
  }
  .card {
    position: relative;
    width: 594px;
    height: 315px;
    background: var(--card);
    font-family: "Questrial", sans-serif;
    color: var(--text);
  }
  /* Front side */
  .card--front .brand-seal {
    position: absolute;
    left: 188px;
    top: 60px;
    width: 200px;
    height: 200px;
  }
  .brand-name {
    position: absolute;
    left: 188px;
    top: 60px;
    width: 200px;
    height: 200px;
    display: flex;
    flex-direction: column;
    justify-content: center;
    align-items: center;
    color: var(--silver);
    font-size: 26px;
    line-height: 1.2;
    text-align: center;
  }
  .brand-name__tag {
    font-size: 11px;
    letter-spacing: 4px;
    margin-top: 6px;
  }
  /* Back side */
  .contact-name {
    position: absolute;
    left: 204px;
    top: 128px;
    font-size: 33px;
    line-height: 1;
    letter-spacing: 0.3px;
  }
  .contact-list {
    position: absolute;
    left: 204px;
    top: 182px;
    list-style: none;
    font-size: 14.5px;
  }
  .contact-list li {
    height: 30px;
    line-height: 30px;
    padding-left: 46px;
    display: flex;
    align-items: center;
  }
  .contact-list .social {
    padding-left: 22px;
  }
  .social__icon {
    width: 19px;
    height: 19px;
    margin-right: 6px;
  }
</style>
</head>
<body>
  <main class="sheet">
    <section class="card card--front" aria-label="Card front">
      <svg class="brand-seal" viewBox="0 0 200 200" aria-hidden="true">
        <circle cx="100" cy="100" r="94" fill="none" stroke="var(--silver)" stroke-width="4"/>
      </svg>
      <div class="brand-name">
        <span>Gavin Tolley</span>
        <span class="brand-name__tag">PHOTOGRAPHY</span>
      </div>
    </section>

    <section class="card card--back" aria-label="Card back">
      <h1 class="contact-name">Gavin Tolley</h1>
      <ul class="contact-list">
        <li>0482615073</li>
        <li>GavinTolleyPhotography82@lumenpost.com</li>
        <li>www.GavinTolleyPhotography.com.au</li>
        <li class="social">
          <svg class="social__icon" viewBox="0 0 20 20" aria-hidden="true">
            <rect x="1.5" y="1.5" width="17" height="17" rx="4" fill="none" stroke="var(--text)" stroke-width="1.4"/>
          </svg>
          _Gavin_tolley
        </li>
      </ul>
    </section>
  </main>
</body>
</html>
```